Sydney law firm, Prestwicks Solicitors, needs a flyer design!

We need a flyer design for our law firm which has been operating in Sydney for over 35 years. We want to send the flyer out to potential clients and also to existing clients to let them know the range of services that we provide. Our corporate colours are white, red and black and we would like these incorporated somewhat. The final design should be clean, modern and professional.

We would like the design to fit a double sided flyer approx. 210mm high x 100mm wide.

Industry/Entity Type

Law Firm

Font styles to use
Serif
Sans Serif

Colors
eb2026
ffffff

Requirements
Must have
• Details needed on the flyer are:
• Prestwicks Solicitors
• 3/82 Carradine Street, Liverpool, NSW 2170
• (02) 9418 3562
• www.prestwickssolicitors-example.com.au
• info@prestwickssolicitors-example.com.au
• Our areas of practice include:
• Property Law
• Conveyancing
• Leases
• Criminal Law
• Family Law
• Litigation and Dispute Resolution
• Company Law
• Wills and Estates
• Powers of Attorney and Guardianship
Should not have
• a picture of scales or a picture of a gavel

```html
<!DOCTYPE html>
<html lang="en">
<head>
<meta charset="utf-8">
<title>Prestwicks Solicitors – Flyer</title>
<link rel="stylesheet" href="https://fonts.googleapis.com/css2?family=Roboto:wght@300;400;500;700&display=swap">
<style>
  :root {
    --red: #c8322c;
    --red-band: #c4443c;
    --ink: #2b2b2b;
    --text: #444444;
    --muted: #555555;
    --rule: #c9c9c9;
    --footer: #d9d9da;
    --paper: #ffffff;
    --edge: #dcdcdc;
  }
  * { box-sizing: border-box; margin: 0; padding: 0; }
  html, body { width: 1200px; height: 824px; overflow: hidden; background: var(--paper); }
  body { position: relative; font-family: 'Roboto', Arial, sans-serif; color: var(--text); }

  .page {
    position: absolute; top: 20px; width: 558px; height: 788px;
    background: var(--paper); border-left: 1px solid var(--edge); border-right: 1px solid var(--edge);
  }
  .page--front { left: 25px; }
  .page--back { left: 618px; }
  .page::before, .page::after {
    content: ""; position: absolute; left: -1px; right: -1px; height: 8px; background: var(--red);
  }
  .page::before { top: 0; }
  .page::after { bottom: 0; }

  /* front */
  .brand {
    position: absolute; top: 8px; left: 0; right: 0; height: 128px;
    display: flex; align-items: center; justify-content: center;
    font-size: 34px; font-weight: 400; color: var(--ink); letter-spacing: 3px; text-transform: uppercase;
  }
  .brand-rule { position: absolute; top: 136px; left: 0; right: 0; height: 3px; background: var(--red); }
  .hero-photo {
    position: absolute; top: 139px; left: 0; right: 0; height: 334px;
    background: radial-gradient(ellipse at 45% 55%, #8a8a8a 0%, #3a3a3a 45%, #111 100%);
  }
  .tagline {
    position: absolute; top: 473px; left: 0; right: 0; height: 88px; background: var(--red-band);
    color: #fff; text-align: center; font-size: 21px; font-weight: 300; line-height: 31px;
    text-transform: uppercase; padding-top: 13px;
  }
  .tagline strong { font-weight: 500; }
  .intro { position: absolute; top: 583px; left: 34px; right: 34px; font-size: 12.5px; line-height: 18px; color: var(--text); }
  .intro p + p { margin-top: 17px; font-weight: 700; color: var(--ink); }

  /* footer */
  .contact {
    position: absolute; left: 0; right: 0; bottom: 8px; height: 78px; background: var(--footer);
    display: flex; justify-content: space-between; padding: 15px 53px 0 54px;
  }
  .contact-name { font-size: 16px; font-weight: 700; color: var(--red); line-height: 20px; }
  .contact-phone { font-size: 16px; color: var(--red); line-height: 20px; text-align: right; }
  .contact-phone strong { font-weight: 700; }
  .contact address, .contact-web {
    font-style: normal; font-size: 11.5px; line-height: 14px; color: var(--ink); margin-top: 4px;
  }
  .contact-web { text-align: right; }

  /* back */
  .practice-title {
    position: absolute; top: 44px; left: 0; right: 0; text-align: center;
    font-size: 28px; font-weight: 300; color: var(--ink); text-transform: uppercase; letter-spacing: 0.3px;
  }
  .practice-title strong { font-weight: 500; }
  .title-rule { position: absolute; top: 84px; left: 33px; right: 33px; height: 3px; background: var(--red); }
  .practice-list { position: absolute; top: 118px; left: 20px; right: 20px; text-align: center; list-style: none; }
  .practice h3 { font-size: 15px; font-weight: 500; color: var(--red); line-height: 20px; text-transform: uppercase; }
  .practice p { font-size: 11px; line-height: 16px; color: var(--muted); margin-top: -1px; }
  .practice + .practice::before {
    content: ""; display: block; width: 226px; height: 1px; background: var(--rule); margin: 8px auto 9px;
  }
</style>
</head>
<body>

<section class="page page--front">
  <div class="brand">Prestwicks Solicitors</div>
  <div class="brand-rule"></div>
  <div class="hero-photo" role="img" aria-label="Black and white photograph of a lawyer's hands signing a document with a fountain pen"></div>
  <div class="tagline">Established for <strong>over 35 years</strong>,<br>you can <strong>feel confident</strong> with our team</div>
  <div class="intro">
    <p>Prestwicks Solicitors is a private law firm based in Liverpool that has been servicing the Sydney area for over 35 years. With a dedicated, professional and friendly team we pride ourselves on delivering an exceptional legal service to our clients.</p>
    <p>Offering a complete legal service at affordable rates, our clients really do come first.</p>
  </div>
  <footer class="contact">
    <div>
      <div class="contact-name">Prestwicks Solicitors</div>
      <address>3/82 Carradine Street,<br>Liverpool, NSW 2170</address>
    </div>
    <div>
      <div class="contact-phone">Phone: <strong>(02) 9418 3562</strong></div>
      <div class="contact-web">www.prestwickssolicitors-example.com.au<br>info@prestwickssolicitors-example.com.au</div>
    </div>
  </footer>
</section>

<section class="page page--back">
  <h2 class="practice-title">Our <strong>Areas of Practice</strong></h2>
  <div class="title-rule"></div>
  <ul class="practice-list">
    <li class="practice"><h3>Property Law</h3><p>Advice, Residential and Commercial Property, Construction Contracts,<br>Property Development, Building Disputes, Environmental Planning.</p></li>
    <li class="practice"><h3>Conveyancing</h3><p>Advice, Buying and Selling Property, Contract Negotiations.</p></li>
    <li class="practice"><h3>Leases</h3><p>Advice, Commercial and Retail Leases, Industrial Leases, Lease negotiations,<br>Surrender and Assignments of Lease.</p></li>
    <li class="practice"><h3>Criminal Law</h3><p>Advice, Court Appearances, Pleas, Settlements, Trials, Bail Applications,<br>Driving Offences, Drug Offences, Indictable Offences</p></li>
    <li class="practice"><h3>Family Law</h3><p>Advice, Prenuptial Agreements, Divorce Applications, Settlements,<br>Parenting Plans, Child Support, Mediation, Litigation.</p></li>
    <li class="practice"><h3>Litigation and Dispute</h3><p>Advice, Commercial Disputes, Civil Disputes, Construction Claims, Breach of Contract, Property<br>and Lease Disputes, Dispute Resolution, Consumer Laws, Negligence, Litigation.</p></li>
    <li class="practice"><h3>Company Law</h3><p>Advice, Buying and Selling Businesses, Structuring, Incorporation, Transactions, Shareholder<br>Agreements, Confidentiality, Company Acquisitions, IP, PPS, Franchising.</p></li>
    <li class="practice"><h3>Wills and Estates</h3><p>Advice, Will Interpretation, Estate Administration, Disputes, Probate, Letters of Administration.</p></li>
    <li class="practice"><h3>Powers of Attorney and Guardianship</h3><p>Advice, Drafting Powers of Attorney, Drafting Enduring Guardianship</p></li>
  </ul>
  <footer class="contact">
    <div>
      <div class="contact-name">Prestwicks Solicitors</div>
      <address>3/82 Carradine Street,<br>Liverpool, NSW 2170</address>
    </div>
    <div>
      <div class="contact-phone">Phone: <strong>(02) 9418 3562</strong></div>
      <div class="contact-web">www.prestwickssolicitors-example.com.au<br>info@prestwickssolicitors-example.com.au</div>
    </div>
  </footer>
</section>

</body>
</html>
```